Professional modern business card design

A business card for my nutrition business, wanting a professional look, with info clearly visible. Open to using logo colours too.

Would like key info on the front -
logo
my name and qualifications
email
phone number

and just an enlarged logo again / image on the back.

```html
<!DOCTYPE html>
<html lang="en">
<head>
<meta charset="utf-8">
<title>Fennel Nutrition – Business Card</title>
<link href="https://fonts.googleapis.com/css2?family=Noto+Sans:wght@400;600;700&display=swap" rel="stylesheet">
<style>
  :root {
    --backdrop: #ababab;
    --card: #ffffff;
    --navy: #0f2b3c;
    --lime: #cfd92a;
    --photo-yellow: #f1e3a8;
    --photo-sage: #c9d2bf;
    --photo-red: #e3a49c;
    --photo-cream: #ece6dc;
  }
  * { margin: 0; padding: 0; box-sizing: border-box; }
  html, body {
    width: 1200px; height: 1000px; overflow: hidden;
    background: var(--backdrop);
    font-family: "Noto Sans", Arial, sans-serif;
    color: var(--navy);
  }
  .card {
    position: absolute; left: 293px; top: 323px;
    width: 615px; height: 354px;
    background: var(--card);
    overflow: hidden;
  }
  .card__photo {
    position: absolute; left: 240px; top: 0; right: 0; bottom: 0;
    background: linear-gradient(160deg,
      var(--photo-yellow) 0%,
      var(--photo-sage) 38%,
      var(--photo-cream) 62%,
      var(--photo-red) 100%);
    -webkit-mask-image: linear-gradient(100deg, transparent 8%, rgba(0,0,0,.55) 45%, #000 75%);
    mask-image: linear-gradient(100deg, transparent 8%, rgba(0,0,0,.55) 45%, #000 75%);
  }
  .brand {
    position: absolute; left: 38px; top: 52px;
    display: flex; align-items: flex-start; gap: 10px;
  }
  .brand__mark {
    width: 12px; height: 12px; margin-top: 12px;
    background: var(--lime);
  }
  .brand__name {
    font-weight: 700; color: var(--navy);
    font-size: 30px; line-height: 32px;
  }
  .person {
    position: absolute; left: 37px; top: 194px;
  }
  .person__name { font-size: 29px; font-weight: 700; line-height: 38px; }
  .person__role { font-size: 14.5px; font-weight: 400; line-height: 20px; }
  .contact {
    position: absolute; left: 38px; top: 282px;
    font-size: 17.5px; font-weight: 600; line-height: 23px;
  }
  .web {
    position: absolute; right: 54px; top: 308px;
    font-size: 17.5px; font-weight: 400; color: var(--navy);
  }
  .web__main { font-weight: 700; color: var(--navy); }
  .web__accent { font-weight: 700; color: var(--lime); }
</style>
</head>
<body>
  <div class="card">
    <div class="card__photo" role="img" aria-label="Soft-focus photograph of fresh vegetables – peppers, fennel and chillies – beside a ceramic jug and a cookbook"></div>

    <div class="brand">
      <span class="brand__mark"></span>
      <div class="brand__name">Fennel<br>Nutrition</div>
    </div>

    <div class="person">
      <p class="person__name">Harriet Lane</p>
      <p class="person__role">Specialist Rehabilitation Dietitian</p>
    </div>

    <div class="contact">
      <p class="contact__phone">07700900418</p>
      <p class="contact__email">harriet@fennelnutrition.co.uk</p>
    </div>

    <p class="web"><span class="web__main">fennel</span><span class="web__accent">nutrition</span>.co.uk</p>
  </div>
</body>
</html>
```